Hello Creative Minds!
Our business is after a elegant and classy flyer that draws attention!
The business is Velmora Turf - Lawn Rejuvenation Services. We provide services that maintain a healthy and vibrant green lawn through the tough Australian seasons. The products we use limits the water needed to keep grass green to a minimum - practically none at all! This not only helps the home owner or home seller but the environment by limiting the use of water that is needed to create a green lawn. The products we use are made from natural ingredients that are and pet friendly.
This fly will be our introductory offer to the market. Below are the required points that need to be on the flyer. Attached is the business logo, before & after pictures and 1 example of the LAYOUT not DESIGN of what the flyer should be laid out like or similar to. Feel free to use different 'Lawn Mower' pictures.
All the best; if you need any questions answered please feel free to message.
REQUIRED POINTS (Please re-phrase were possible);
*Instantly restores the natural green colour of grass – year round
*Lasts for up to 3 months
*Substantially reduces watering needs
*Pet friendly
*Stays green during droughts and water restrictions
*UV fade resistant
*Won’t bleed, run, or stain once absorbed into the grass
*Safe for the environment, pets and people
*Works in extreme heat, cold and frost
*Organic and natural – no harmful chemicals
*Reduces the amount of fertilizer
and water used on lawns
*Kerb appeal is essential for getting your property sold for the highest price possible
SERVICES & PRICING
Lawn maintenance (cut & trim) starting from $60
Lawn rejuvenation starting from $80 (Only $27 a month for 3 months)*
Package deal starting from $120
Introductory offer: 25% off all services. Refer a friend, when they book you receive another 25% off your next service.
LOCATIONS
Nowra to Sydney
CONTACT NUMBER
Will be posted with the winner - please leave an area for this.
SOCIAL MEDIA
Please add Chatterloop and Snapvista logo's
Updates
Competition has finished, thank you to all that have participated! I will review and comment on the flyers that need assistance. All the best with future designs!
Target Market(s)
home owners, home sellers, property developers, real estates and nursing homes and government housing.
Industry/Entity Type
Lawn Care
Look and feel
Each slider illustrates characteristics of the customer's brand and the style your logo design should communicate.

```html
<!DOCTYPE html>
<html lang="en">
<head>
<meta charset="utf-8">
<title>Velmora Turf – Lawn Rejuvenation Services Flyer</title>
<link rel="stylesheet" href="https://fonts.googleapis.com/css2?family=Yellowtail&family=Montserrat:wght@500;600;700&family=Lato:wght@400;700&family=Oswald:wght@500&display=swap">
<style>
  :root{
    --navy:#1e2836;
    --backdrop:#d6d6d6;
    --white:#ffffff;
    --lime:#d3e04a;
    --leaf:#6fa83a;
    --deep-leaf:#4e8a2f;
    --offer-red:#d3242a;
    --rule:#e9ecef;
    --muted:#dfe3e8;
  }
  *{box-sizing:border-box;margin:0;padding:0}
  html,body{width:1200px;height:1096px;overflow:hidden;background:var(--backdrop)}
  body{font-family:"Lato",sans-serif;color:var(--white)}
  .flyer{position:absolute;left:226px;top:20px;width:748px;height:1056px;background:var(--navy);box-shadow:0 6px 18px rgba(0,0,0,.25)}
  .abs{position:absolute}

  .headline{left:28px;top:30px;width:700px;font-family:"Yellowtail",cursive;font-weight:400;font-size:88px;line-height:.92;
    background:linear-gradient(100deg,var(--lime) 10%,#a8c83c 45%,var(--leaf) 85%);
    -webkit-background-clip:text;background-clip:text;color:transparent;
    filter:drop-shadow(3px 4px 3px rgba(0,0,0,.55));z-index:5}
  .headline .line2{display:block;padding-left:210px}

  .photo-frame{left:150px;top:190px;width:440px;height:440px;border:2px solid var(--rule)}
  .photo{left:163px;width:420px;height:214px}
  .photo-before{top:172px;background:linear-gradient(180deg,#8d9492 0%,#8a918f 30%,#b4c46a 45%,#a9be59 60%,#6e7378 72%,#5d6268 100%)}
  .photo-after{top:388px;background:linear-gradient(180deg,#7f8785 0%,#858c8a 32%,#4f9a3a 48%,#57a03e 62%,#64696f 74%,#555a60 100%)}

  .swatch{border-radius:50%;border:3px solid var(--white);box-shadow:0 4px 10px rgba(0,0,0,.5)}
  .swatch-before{left:70px;top:148px;width:164px;height:164px;background:radial-gradient(circle at 40% 40%,#d8c08d,#b69a62 60%,#8e7546)}
  .swatch-after{left:481px;top:296px;width:164px;height:164px;background:radial-gradient(circle at 45% 40%,#6fb446,#3f8a2b 60%,#2c6a1f);
    display:flex;align-items:center;justify-content:center;text-align:center;
    font-family:"Montserrat",sans-serif;font-weight:600;font-size:17px;line-height:1.15;text-shadow:0 2px 3px rgba(0,0,0,.8);letter-spacing:.5px}
  .arc-label{overflow:visible;font-family:"Montserrat",sans-serif;font-weight:700;font-size:15px;letter-spacing:6px;fill:var(--white)}

  .offer{left:39px;top:331px;width:265px;height:122px;z-index:4;filter:drop-shadow(2px 3px 4px rgba(0,0,0,.5))}
  .offer-text{left:46px;top:338px;width:232px;text-align:center;z-index:5;font-family:"Montserrat",sans-serif}
  .offer-text .kicker{font-weight:600;font-size:15px}
  .offer-text .big{font-weight:700;font-size:34px;line-height:1}
  .offer-text .all{font-weight:600;font-size:17px;line-height:1.1}
  .offer-text .refer{font-family:"Lato",sans-serif;font-weight:700;font-size:10.5px;line-height:1.35;margin-top:5px}

  .panel{border:1.5px solid var(--rule)}
  .panel-title{position:absolute;top:-10px;left:0;right:0;text-align:center;font-family:"Montserrat",sans-serif;font-weight:600;font-size:14px}
  .panel-title span{background:var(--navy);padding:0 5px}
  .benefits{left:52px;top:652px;width:420px;height:226px}
  .benefit-col{position:absolute;top:20px;list-style:none;font-size:11px;line-height:1.35;color:var(--muted)}
  .benefit-col li{position:relative;padding-left:13px;margin-bottom:5px}
  .benefit-col li::before{content:"✓";position:absolute;left:0;top:0;color:var(--lime);font-weight:700}
  .col-left{left:14px;width:195px}
  .col-right{left:218px;width:190px}

  .pricing{left:491px;top:642px;width:219px;height:200px;padding:24px 0 0 18px}
  .svc-name{font-family:"Montserrat",sans-serif;font-weight:600;font-size:12.5px;color:var(--lime);margin-top:4px}
  .svc-price{font-size:11.5px;color:var(--muted);margin-bottom:8px}
  .svc-price b{font-family:"Montserrat",sans-serif;font-size:16px;color:var(--white)}

  .brand{left:120px;top:905px;width:360px;display:flex;align-items:center;gap:12px;justify-content:center}
  .brand-dot{width:18px;height:18px;border-radius:50%;background:var(--leaf)}
  .brand-name{font-family:"Montserrat",sans-serif;font-weight:600;font-size:40px;color:var(--white)}

  .call{left:82px;top:1000px;white-space:nowrap;display:flex;align-items:baseline;gap:10px}
  .call-label{font-family:"Montserrat",sans-serif;font-weight:700;font-size:22px}
  .call-number{font-family:"Oswald",sans-serif;font-weight:500;font-size:34px;letter-spacing:2px;
    background:linear-gradient(90deg,var(--lime),var(--leaf));-webkit-background-clip:text;background-clip:text;color:transparent}

  .contacts{left:542px;top:895px;list-style:none}
  .contacts li{display:flex;align-items:center;gap:8px;height:30px;margin-bottom:12px;font-size:11.5px;color:var(--muted)}
  .contact-icon{width:30px;height:30px;border-radius:3px;background:linear-gradient(135deg,var(--lime),var(--leaf));display:flex;align-items:center;justify-content:center}
</style>
</head>
<body>
<main class="flyer">
  <h1 class="abs headline">Make your lawn <span class="line2">great again!</span></h1>

  <div class="abs photo-frame"></div>
  <div class="abs photo photo-before" role="img" aria-label="Backyard lawn before treatment, patchy pale grass beside grey fence and paved patio"></div>
  <div class="abs photo photo-after" role="img" aria-label="Same backyard lawn after treatment, even green grass beside grey fence and paved patio"></div>

  <div class="abs swatch swatch-before" role="img" aria-label="Close-up of dry brown grass"></div>
  <svg class="abs arc-label" style="left:52px;top:130px" width="200" height="200" viewBox="0 0 200 200" aria-hidden="true">
    <path id="arc-before" d="M13.5 131.5 A92 92 0 0 1 116 9.4" fill="none"/>
    <text><textPath href="#arc-before">BEFORE</textPath></text>
  </svg>

  <div class="abs swatch swatch-after" role="img" aria-label="Close-up of lush green grass">LASTS<br>FOR UP TO<br>3 MONTHS</div>
  <svg class="abs arc-label" style="left:463px;top:278px" width="200" height="200" viewBox="0 0 200 200" aria-hidden="true">
    <path id="arc-after" d="M123.8 11.1 A92 92 0 0 1 190.6 116" fill="none"/>
    <text><textPath href="#arc-after">AFTER</textPath></text>
  </svg>

  <svg class="abs offer" viewBox="0 0 265 122" aria-hidden="true">
    <polygon points="1,1 242,1 264,61 242,121 1,121" fill="var(--offer-red)" stroke="var(--white)" stroke-width="1.5"/>
  </svg>
  <div class="abs offer-text">
    <p class="kicker">INTRODUCTORY OFFER:</p>
    <p class="big">25% OFF</p>
    <p class="all">ALL SERVICES</p>
    <p class="refer">REFER A FRIEND: When they book, you will receive 25% OFF your next service!</p>
  </div>

  <section class="abs panel benefits">
    <h2 class="panel-title"><span>DIRECT BENEFITS</span></h2>
    <ul class="benefit-col col-left">
      <li>Instantly restores the natural green colour of grass – year round</li>
      <li>Substantially reduces watering needs</li>
      <li>Pet friendly</li>
      <li>Stays green during droughts and water restrictions</li>
      <li>Organic and natural – no harmful chemicals</li>
      <li>Won’t bleed, run, or stain once absorbed into the grass</li>
    </ul>
    <ul class="benefit-col col-right">
      <li>Safe for the environment, pets and people</li>
      <li>Works in extreme heat, cold and frost</li>
      <li>UV fade resistant</li>
      <li>Reduces the amount of fertilizer and water used on lawns</li>
      <li>Kerb appeal is essential for getting your property sold for the highest price possible</li>
    </ul>
  </section>

  <section class="abs panel pricing">
    <h2 class="panel-title"><span>SERVICES &amp; PRICING</span></h2>
    <p class="svc-name">LAWN MAINTENANCE</p>
    <p class="svc-price">Starting from <b>$60</b></p>
    <p class="svc-name">LAWN REJUVENATION</p>
    <p class="svc-price">Starting from <b>$80</b></p>
    <p class="svc-name">PACKAGE DEAL</p>
    <p class="svc-price">Starting from <b>$120</b></p>
    <p class="svc-name">LOCATIONS</p>
    <p class="svc-price">Nowra to Sydney</p>
  </section>

  <div class="abs brand">
    <span class="brand-dot"></span>
    <span class="brand-name">Velmora Turf</span>
  </div>

  <p class="abs call"><span class="call-label">CALL US TODAY</span><span class="call-number">02 5550 0199</span></p>

  <ul class="abs contacts">
    <li><span class="contact-icon">
      <svg width="18" height="13" viewBox="0 0 18 13" aria-hidden="true"><rect x="1" y="1" width="16" height="11" fill="none" stroke="var(--navy)" stroke-width="1.6"/><path d="M1 1 L9 7.5 L17 1" fill="none" stroke="var(--navy)" stroke-width="1.6"/></svg>
    </span>velmoraturf@mailbox.example</li>
    <li><span class="contact-icon" aria-label="Chatterloop"></span>@velmoraturf</li>
    <li><span class="contact-icon" aria-label="Snapvista"></span>@velmoraturf</li>
  </ul>
</main>
</body>
</html>
```